Industrial services company requires brochure for new product

We are an industrial services company called Tern Ridge Group. Our clients include major mining, oil and gas and infrastructure clients in Western Australia.

We require a 4 page brochure to feature a new paint removal machine we are bringing to the market in Western Australia.The document will be used predominantly electronically but should be of a quality that can be printed also.

The new machine is an innovative way of removing paint from steel structures as it does not use abrasive blasting to remove the paint. Instead it uses induction heating.

There are some major environmental and safety benefits to using this machine over traditional methods as there are no airborne particles, no noise and minimal waste. The environmental and safety benefits of the are the competitive advantage of the machine and should come through in the marketing.

I have provided as an attachment the proposed copy, the pics available for use, and the Tern Ridge logo.

In general I am thinking page 1 (cover - hero pic/company logo), page 2 (machine information), page 3 (case study) page 4 (about us/contact details/logo etc) but am happy to look at other options.

The images I have attached are the highest quality I will have available.

Target Market(s)

Mining, oil and gas, government infrastructure clients. These are businesses

Industry/Entity Type

Oil And Gas

Requirements
Must have
• The majority of the text supplied as necessary to understand the technology.

```html
<!DOCTYPE html>
<html lang="en">
<head>
<meta charset="utf-8">
<title>How It Works – Page Two Options</title>
<link href="https://fonts.googleapis.com/css2?family=Montserrat:wght@400;600;700&family=Open+Sans:ital,wght@0,400;0,700;1,400&display=swap" rel="stylesheet">
<style>
:root{
  --board:#c9ccd0;
  --paper:#ffffff;
  --ink:#333333;
  --body:#555555;
  --blue:#1b9ad6;
  --charcoal:#333333;
  --black:#0a0a0a;
  --photo-orange:#d9662c;
  --photo-steel:#8d9196;
  --photo-dark:#4a4d50;
}
*{box-sizing:border-box;margin:0;padding:0}
html,body{width:1200px;height:1000px;overflow:hidden}
body{background:var(--board);font-family:"Open Sans",Arial,sans-serif;color:var(--body);position:relative}
.board-title{position:absolute;left:498px;top:121px;width:206px;height:26px;background:var(--black);color:#fff;
  font:400 15px/26px "Montserrat",Arial,sans-serif;letter-spacing:9px;text-align:center}
.option-number{position:absolute;top:198px;font:700 17px "Montserrat",Arial,sans-serif;color:var(--black)}
.page{position:absolute;top:247px;width:362px;height:516px;background:var(--paper);overflow:hidden;
  box-shadow:0 4px 10px rgba(0,0,0,.35)}
.page > *{position:absolute;z-index:2}
.page > [role="img"]{z-index:1}
.page-one{left:50px}.page-two{left:420px;width:360px}.page-three{left:790px;width:360px}
.title{font-family:"Montserrat",Arial,sans-serif;line-height:.9;text-transform:uppercase}
.title .small{display:block;font-size:22px;font-weight:600}
.title .big{display:block;font-size:34px;font-weight:700}
.subtitle{font-family:"Montserrat",Arial,sans-serif;font-size:10px;white-space:nowrap}
.copy{font-size:6px;line-height:1.45}
.copy p + p{margin-top:8px}
.heading{font:700 7px/1.25 "Montserrat",Arial,sans-serif;color:var(--ink);text-transform:uppercase}
.bullets{list-style:none;margin:6px 0 0}
.bullets li::before{content:"• ";color:var(--blue)}
.footer{left:0;bottom:0;width:100%;height:25px;color:#fff;text-align:center;
  font:400 7px/25px "Open Sans",Arial,sans-serif;letter-spacing:3px}
.photo-worker{background:linear-gradient(135deg,var(--photo-steel),var(--photo-orange) 55%,var(--photo-dark))}
.photo-machine{background:radial-gradient(ellipse at 55% 45%,#3d4a44,#8a9a94 50%,#ffffff 72%)}
.photo-unit{background:linear-gradient(160deg,#9a9ea2,#c7cacd 45%,#5d6165)}
.photo-site{background:linear-gradient(150deg,#b9bcbf,#7c8185 60%,#cc6a38)}
.diagram{background:linear-gradient(180deg,#eef6f0,#cfe6d6 60%,#9cc3d8)}
/* page one */
.page-one .hero-circle{left:-12px;top:-8px;width:180px;height:180px;border-radius:50%;border:6px solid #fff}
.page-one .title{left:168px;top:16px;color:var(--blue)}
.page-one .title .big{margin-left:10px}
.page-one .subtitle{left:193px;top:63px;color:#888}
.page-one .intro{left:190px;top:97px;width:162px}
.page-one .safe-head{left:20px;top:195px;width:150px}
.page-one .safe-copy{left:20px;top:216px;width:150px}
.page-one .avail-head{left:180px;top:195px;width:175px}
.page-one .avail-copy{left:180px;top:216px;width:170px}
.page-one .diagram{left:180px;top:285px;width:118px;height:68px}
.page-one .unit-copy{left:20px;top:333px;width:135px}
.page-one .unit-circle{left:240px;top:295px;width:190px;height:190px;border-radius:50%}
.page-one .machine-small{left:165px;top:398px;width:78px;height:70px;border-radius:6px}
.page-one .footer{background:var(--blue)}
/* page two */
.page-two .title{left:20px;top:16px;color:var(--ink)}
.page-two .title .big{font-size:32px}
.page-two .subtitle{left:132px;top:49px;color:var(--blue)}
.page-two .intro{left:20px;top:72px;width:130px}
.page-two .machine{left:236px;top:12px;width:116px;height:165px}
.page-two .shot-a{left:20px;top:190px;width:135px;height:68px}
.page-two .shot-b{left:20px;top:262px;width:135px;height:68px}
.page-two .safe-head{left:163px;top:194px;width:190px}
.page-two .safe-copy{left:163px;top:212px;width:187px}
.page-two .avail-head{left:20px;top:339px}
.page-two .avail-copy{left:20px;top:355px;width:330px}
.page-two .unit-copy{left:20px;top:392px;width:160px}
.page-two .unit-photo{left:190px;top:395px;width:152px;height:85px}
.page-two .footer{background:var(--charcoal)}
/* page three */
.page-three .title{left:18px;top:14px;color:var(--blue);display:flex;align-items:flex-end;gap:4px}
.page-three .title .big{font-size:32px}
.page-three .subtitle{left:20px;top:42px;color:var(--ink)}
.page-three .intro{left:20px;top:60px;width:172px;font-style:italic}
.page-three .machine{left:238px;top:8px;width:110px;height:115px}
.page-three .diagram{left:212px;top:132px;width:138px;height:78px;transform:rotate(-4deg);box-shadow:0 2px 5px rgba(0,0,0,.3)}
.page-three .safe-head{left:20px;top:157px;width:160px}
.page-three .safe-copy{left:20px;top:184px;width:150px}
.page-three .avail-head{left:20px;top:304px}
.page-three .avail-copy{left:20px;top:323px;width:168px}
.page-three .unit-copy{left:20px;top:383px;width:165px}
.page-three .closing{left:20px;top:465px;font-style:italic}
.page-three .shot-a{left:178px;top:218px;width:124px;height:74px;clip-path:polygon(10% 0,100% 8%,92% 100%,0 88%)}
.page-three .shot-b{left:196px;top:300px;width:138px;height:88px;clip-path:polygon(0 10%,92% 0,100% 90%,8% 100%)}
.page-three .shot-c{left:196px;top:394px;width:138px;height:92px;clip-path:polygon(6% 0,100% 6%,94% 100%,0 94%)}
.page-three .footer{background:var(--black)}
</style>
</head>
<body>
<div class="board-title">PAGE TWO</div>
<div class="option-number" style="left:229px">1</div>
<div class="option-number" style="left:594px">2</div>
<div class="option-number" style="left:963px">3</div>

<section class="page page-one">
  <div class="hero-circle photo-worker" role="img" aria-label="Worker in orange coveralls operating the induction tool on a steel deck"></div>
  <div class="diagram" role="img" aria-label="Diagram of coating removal by controlled induction heating over a steel substrate"></div>
  <div class="unit-circle photo-unit" role="img" aria-label="Stainless steel induction unit on site"></div>
  <div class="machine-small photo-machine" role="img" aria-label="Induction power unit with coiled cable and hand tool"></div>
  <h1 class="title"><span class="small">How it</span><span class="big">Works</span></h1>
  <div class="subtitle">Machine Information</div>
  <div class="copy intro"><p>Induction paint and surface coatings Heatlifter removes steel by the induction principle. Heat is generated in the steel substrate and the bond is broken. The coating was completely removed without disintegrating and completely free of contamination such as grit. Even within the pits and fissures on the surface was severed or detached coating.</p></div>
  <h2 class="heading safe-head">A Safe Environment Friendlyalternative</h2>
  <div class="copy safe-copy">
    <p>The induction Heatlifter is especially effective in removing asbestos, lead, coal tar and other toxic coatings without compromising the health of operators or medium ambiente. Its benefits include:</p>
    <ul class="bullets"><li>No dust particles or airborne</li><li>No noise - the machine is virtually silent</li><li>No waste contaminated water or washed</li><li>No media contaminated ovens</li></ul>
    <p style="margin-top:0">Assets owners value the opportunity to remove toxic paint and coatings without pollution risks. No other</p>
  </div>
  <h2 class="heading avail-head">Available for next maintenance project</h2>
  <div class="copy avail-copy"><p>Maintenance service provider Tern Ridge Group Pty Ltd has invested in this worldwide patented, proven technology Norwegian manufacturer Fjordvarme Technologies A / S to provide its customers in Western Australia, with access to a method of removing paint and coatings alternative.</p></div>
  <div class="copy unit-copy"><p>The Heatlifter induction is a plug and play unit that is easy to mobilize and install anywhere. Tern Ridge Group staff have achieved their Verification Competition (COV) for the operation of the induction Heatlifter and have proven experience in using the equipment in maintenance projects .</p><p>Why not ask us for a quote on your next project maintenance?</p></div>
  <div class="footer">www.ternridgegroup.com.au</div>
</section>

<section class="page page-two">
  <div class="machine photo-machine" role="img" aria-label="Induction power unit with coiled cable and hand tool"></div>
  <div class="shot-a photo-site" role="img" aria-label="Induction tool working on a steel deck"></div>
  <div class="shot-b photo-worker" role="img" aria-label="Worker in orange coveralls using the induction tool"></div>
  <div class="unit-photo photo-unit" role="img" aria-label="Stainless steel induction unit on site"></div>
  <h1 class="title"><span class="small">How it</span><span class="big">Works</span></h1>
  <div class="subtitle">Machine Information</div>
  <div class="copy intro"><p>Induction paint and surface coatings Heatlifter removes steel by the induction principle. Heat is generated in the steel substrate and the bond is broken. The coating was completely removed without disintegrating and completely free of contamination such as grit. Even within the pits and fissures on the surface was severed or detached coating.</p></div>
  <h2 class="heading safe-head">A Safe Environment Friendlyalternative</h2>
  <div class="copy safe-copy">
    <p>The induction Heatlifter is especially effective in removing asbestos, lead, coal tar and other toxic coatings without compromising the health of operators or medium ambiente. Its benefits include:</p>
    <ul class="bullets"><li>No dust particles or airborne</li><li>No noise - the machine is virtually silent</li><li>No waste contaminated water or washed</li><li>No media contaminated ovens</li></ul>
    <p style="margin-top:0">Assets owners value the opportunity to remove toxic paint and coatings without pollution risks. No other system makes it quick, clean and effortless manner.</p>
  </div>
  <h2 class="heading avail-head">Available for next maintenance project</h2>
  <div class="copy avail-copy"><p>Maintenance service provider Tern Ridge Group Pty Ltd has invested in this worldwide patented, proven technology Norwegian manufacturer Fjordvarme Technologies A / S to provide its customers in Western Australia, with access to a method of removing paint and coatings alternative.</p></div>
  <div class="copy unit-copy"><p>The Heatlifter induction is a plug and play unit that is easy to mobilize and install anywhere. Tern Ridge Group staff have achieved their Verification Competition (COV) for the operation of the induction Heatlifter and have proven experience in using the equipment in maintenance projects .</p><p>Why not ask us for a quote on your next project maintenance?</p></div>
  <div class="footer">www.ternridgegroup.com.au</div>
</section>

<section class="page page-three">
  <div class="machine photo-machine" role="img" aria-label="Induction power unit with coiled cable and hand tool"></div>
  <div class="diagram" role="img" aria-label="Diagram of coating removal by controlled induction heating over a steel substrate"></div>
  <div class="shot-a photo-site" role="img" aria-label="Induction tool working on a steel deck"></div>
  <div class="shot-b photo-worker" role="img" aria-label="Worker in orange coveralls using the induction tool"></div>
  <div class="shot-c photo-unit" role="img" aria-label="Stainless steel induction unit on site"></div>
  <h1 class="title"><span class="small">How it</span><span class="big">Works</span></h1>
  <div class="subtitle">Machine Information</div>
  <div class="copy intro"><p>Induction paint and surface coatings Heatlifter removes steel by the induction principle. Heat is generated in the steel substrate and the bond is broken. The coating was completely removed without disintegrating and completely free of contamination such as grit. Even within the pits and fissures on the surface was severed or detached coating.</p></div>
  <h2 class="heading safe-head">A Safe Environment Friendlyalternative</h2>
  <div class="copy safe-copy">
    <p>The induction Heatlifter is especially effective in removing asbestos, lead, coal tar and other toxic coatings without compromising the health of operators or medium ambiente. Its benefits include:</p>
    <ul class="bullets"><li>No dust particles or airborne</li><li>No noise - the machine is virtually silent</li><li>No waste contaminated water or washed</li><li>No media contaminated ovens</li></ul>
    <p style="margin-top:0">Assets owners value the opportunity to remove toxic paint and coatings without pollution risks. No other system makes it quick, clean and effortless manner.</p>
  </div>
  <h2 class="heading avail-head">Available for next maintenance project</h2>
  <div class="copy avail-copy"><p>Maintenance service provider Tern Ridge Group Pty Ltd has invested in this worldwide patented, proven technology Norwegian manufacturer Fjordvarme Technologies A / S to provide its customers in Western Australia, with access to a method of removing paint and coatings alternative.</p></div>
  <div class="copy unit-copy"><p>The Heatlifter induction is a plug and play unit that is easy to mobilize and install anywhere. Tern Ridge Group staff have achieved their Verification Competition (COV) for the operation of the induction Heatlifter and have proven experience in using the equipment in maintenance projects .</p></div>
  <div class="copy closing">Why not ask us for a quote on your next project<br>maintenance?</div>
  <div class="footer">www.ternridgegroup.com.au</div>
</section>
</body>
</html>
```